Company website for an international IT business

We require a website for our business, Korvel Solutions. The business has two primary areas: Futures, which includes two machine learning/deep learning based products and IT consultancy, which is the service we provide to other businesses.

We bridge cutting-edge research to market.

STYLING:
The site can be on single page or multi-page. This is fully open to suggestion. So long as the look and feel are consistent. Currently, we have no strong preference for colors, styles or layouts.
You can find the logo of our website in the attachment “Korvel-logo.png” and “Korvel-logo-landscape.png”.

CONTENT:
You can find the text of the website in “Website-Content.pdf”, which explains the services and products of our business. The format of the text is also open to suggestion - including breaking up the text into visually appealing sections.
We would also like to include suitable images on the website so that it does not appear to be a text-heavy page. We are happy to have placeholder images on stock image sites if needed. We are open to suggestions on placing of images

Industry/Entity Type

It Company

Coding

Coded - Design and coding required

Number of Pages Required

1 page

Colors

Designer to choose colors to be used in the design.

Requirements
Must have
• A full description of the requirement is in the attachment "Website-Content.pdf"
• The design must have HTML/CSS, and all resources relevant (images, fonts etc)
• We are
Nice to have
• We are open to suggestions on top of the requirement, please reach out and communicate.

```html
<!DOCTYPE html>
<html lang="en">
<head>
<meta charset="utf-8">
<title>Korvel Solutions</title>
<link rel="stylesheet" href="https://fonts.googleapis.com/css2?family=Open+Sans:wght@400;600;700;800&display=swap">
<style>
  :root {
    --blue: #1b8cd4;
    --blue-dark: #1577b8;
    --ink: #333333;
    --muted: #777777;
    --band: #2a2a2a;
    --band-2: #333333;
    --footer-dark: #1e1e1e;
    --line: #dddddd;
    --white: #ffffff;
  }
  * { box-sizing: border-box; margin: 0; padding: 0; }
  html, body { width: 1200px; height: 2496px; overflow: hidden; }
  body { font-family: "Open Sans", Arial, sans-serif; color: var(--ink); background: var(--white); position: relative; }

  .site-header { position: absolute; top: 0; left: 0; width: 1200px; height: 140px; background: var(--white); }
  .brand { position: absolute; left: 128px; top: 28px; display: flex; align-items: center; gap: 14px; }
  .brand-mark { width: 78px; height: 78px; border-radius: 50%; background: var(--blue); }
  .brand-name { font-weight: 800; font-size: 30px; letter-spacing: 1px; color: var(--ink); }
  .header-email { position: absolute; right: 128px; top: 22px; font-size: 17px; color: var(--ink); display: flex; align-items: center; gap: 8px; }
  .main-nav { position: absolute; right: 128px; top: 76px; display: flex; gap: 34px; font-size: 14px; }
  .main-nav a { color: var(--ink); text-decoration: none; padding-bottom: 6px; }
  .main-nav a.active { color: var(--blue); border-bottom: 2px solid var(--blue); }

  .hero { position: absolute; top: 140px; left: 0; width: 1200px; height: 462px;
    background: linear-gradient(180deg, #9fc6e6 0%, #c9d9e6 35%, #6f7d88 70%, #3f4a52 100%); }
  .hero-arrow { position: absolute; top: 205px; width: 40px; height: 40px; border-radius: 50%; background: rgba(0,0,0,.55); display: flex; align-items: center; justify-content: center; }
  .hero-arrow.prev { left: 34px; }
  .hero-arrow.next { right: 34px; }

  .intro { position: absolute; top: 630px; left: 0; width: 1200px; text-align: center; color: var(--blue); font-size: 23px; line-height: 34px; font-weight: 600; }

  .services { position: absolute; top: 766px; left: 135px; width: 930px; display: flex; gap: 42px; }
  .service-card { flex: 1; height: 168px; background: var(--blue); color: var(--white); display: flex; flex-direction: column; align-items: center; justify-content: center; gap: 22px; font-size: 18px; }

  .futures { position: absolute; top: 1008px; left: 0; width: 1200px; height: 312px; display: flex; }
  .future { flex: 1; display: flex; gap: 26px; padding: 50px 40px 0 130px; background: var(--band); }
  .future + .future { background: var(--band-2); padding-left: 30px; padding-right: 130px; }
  .future-photo { width: 160px; height: 210px; flex: none; background: linear-gradient(160deg, #7e8f9b, #3d4850); }
  .future-body { color: var(--white); }
  .future-title { font-size: 34px; font-weight: 800; letter-spacing: 1px; margin-top: 4px; }
  .future-text { font-size: 13px; line-height: 20px; color: #b8b8b8; margin: 16px 0 26px; max-width: 250px; }
  .btn-outline { display: inline-block; font-size: 12px; color: var(--white); border: 1px solid #888; padding: 6px 16px; }

  .section-title { text-align: center; font-size: 36px; font-weight: 800; color: var(--blue); letter-spacing: 1px; }
  .consultancy-title { position: absolute; top: 1380px; left: 0; width: 1200px; }
  .consultancy { position: absolute; top: 1462px; left: 130px; width: 940px; display: flex; gap: 40px; }
  .consult-card { flex: 1; height: 180px; border: 1px solid var(--line); box-shadow: 0 2px 6px rgba(0,0,0,.08); display: flex; flex-direction: column; align-items: center; justify-content: center; gap: 20px; text-align: center; font-size: 15px; line-height: 22px; padding: 0 30px; }

  .portfolio { position: absolute; top: 1682px; left: 130px; width: 940px; height: 400px;
    background: linear-gradient(90deg, #7a8a96 0%, #c7cfd6 40%, #5b3a2c 80%, #2a2624 100%); }
  .portfolio-title { position: absolute; top: 40px; left: 0; width: 100%; text-align: center; color: var(--white); font-size: 44px; font-weight: 800; letter-spacing: 1px; }
  .portfolio-panel { position: absolute; top: 104px; left: 252px; width: 436px; height: 230px; background: rgba(27,140,212,.88); color: var(--white); text-align: center; padding: 26px 34px; }
  .portfolio-panel h3 { font-size: 22px; font-weight: 800; letter-spacing: .5px; }
  .portfolio-panel p { font-size: 13px; line-height: 20px; margin: 14px 0 20px; }
  .portfolio-panel .btn-outline { border-color: var(--white); }

  .about-title { position: absolute; top: 2140px; left: 0; width: 1200px; }
  .about-text { position: absolute; top: 2200px; left: 130px; width: 940px; text-align: center; font-size: 14px; line-height: 22px; color: var(--ink); }

  .footer-bar { position: absolute; top: 2338px; left: 0; width: 1200px; height: 54px; background: var(--blue); color: var(--white); font-size: 13px; display: flex; align-items: center; padding: 0 130px; gap: 60px; }
  .footer-bar .item { display: flex; align-items: center; gap: 8px; }
  .social { margin-left: auto; display: flex; gap: 14px; }
  .social span { width: 20px; height: 20px; border-radius: 50%; background: rgba(255,255,255,.85); }
  .footer-bottom { position: absolute; top: 2392px; left: 0; width: 1200px; height: 104px; background: var(--footer-dark); color: #a0a0a0; text-align: center; font-size: 12px; padding-top: 28px; }
  .footer-nav { display: flex; justify-content: center; gap: 14px; margin-bottom: 12px; }
  .footer-nav a { color: #a0a0a0; text-decoration: none; }
</style>
</head>
<body>

<header class="site-header">
  <div class="brand"><span class="brand-mark"></span><span class="brand-name">KORVEL</span></div>
  <div class="header-email">
    <svg width="18" height="14" viewBox="0 0 18 14"><rect x="1" y="1" width="16" height="12" fill="none" stroke="#333" stroke-width="1.6"/><path d="M1 1l8 7 8-7" fill="none" stroke="#333" stroke-width="1.6"/></svg>
    info@korvelsolutions.com
  </div>
  <nav class="main-nav">
    <a class="active" href="#">Home</a><a href="#">Korvel Futures</a><a href="#">IT consultancy</a><a href="#">About Us</a><a href="#">Contact Us</a>
  </nav>
</header>

<section class="hero" role="img" aria-label="Photo of a smiling truck driver standing in front of white lorries under a blue sky">
  <span class="hero-arrow prev"><svg width="14" height="14" viewBox="0 0 14 14"><path d="M9 2L4 7l5 5" fill="none" stroke="#fff" stroke-width="2"/></svg></span>
  <span class="hero-arrow next"><svg width="14" height="14" viewBox="0 0 14 14"><path d="M5 2l5 5-5 5" fill="none" stroke="#fff" stroke-width="2"/></svg></span>
</section>

<p class="intro">Korvel Solutions is an IT consultancy firm with a difference<br>We can provide IT expertise for your business at any stage - from initial idea to live systems</p>

<section class="services">
  <div class="service-card">
    <svg width="44" height="36" viewBox="0 0 44 36" fill="none" stroke="#fff" stroke-width="2"><rect x="3" y="2" width="38" height="24" rx="2"/><path d="M14 34h16M22 26v8M17 11l-4 3 4 3M27 11l4 3-4 3"/></svg>
    Software Development
  </div>
  <div class="service-card">
    <svg width="40" height="40" viewBox="0 0 40 40" fill="none" stroke="#fff" stroke-width="2"><circle cx="20" cy="20" r="5"/><circle cx="6" cy="6" r="3"/><circle cx="34" cy="6" r="3"/><circle cx="6" cy="34" r="3"/><circle cx="34" cy="34" r="3"/><path d="M8 8l8 8M32 8l-8 8M8 32l8-8M32 32l-8-8"/></svg>
    IOT System Design
  </div>
  <div class="service-card">
    <svg width="40" height="40" viewBox="0 0 40 40" fill="none" stroke="#fff" stroke-width="2"><circle cx="15" cy="15" r="6"/><path d="M15 5v3M15 22v3M5 15h3M22 15h3M8 8l2 2M20 20l2 2M22 8l-2 2M8 22l2-2"/><circle cx="29" cy="29" r="4"/><path d="M29 22v2M29 34v2M22 29h2M34 29h2"/></svg>
    Machine learning solutions
  </div>
</section>

<section class="futures">
  <article class="future">
    <div class="future-photo" role="img" aria-label="Photo of a driver sitting in a truck cab"></div>
    <div class="future-body">
      <h2 class="future-title">ORLO</h2>
      <p class="future-text">Our first product learns from live logistics data to plan smarter routes, cut idle hours and keep every fleet moving on time.</p>
      <a class="btn-outline">Read more</a>
    </div>
  </article>
  <article class="future">
    <div class="future-photo" role="img" aria-label="Photo of a truck driver leaning out of a cab window"></div>
    <div class="future-body">
      <h2 class="future-title">AXLEWISE</h2>
      <p class="future-text">A deep learning tool that reads vehicle history and market signals to give buyers an honest value before they commit.</p>
      <a class="btn-outline">Read more</a>
    </div>
  </article>
</section>

<h2 class="section-title consultancy-title">IT CONSULTANCY</h2>
<section class="consultancy">
  <div class="consult-card">
    <svg width="46" height="34" viewBox="0 0 46 34" fill="none" stroke="#333" stroke-width="2"><rect x="2" y="4" width="26" height="20"/><path d="M28 11h9l6 7v6H28z"/><circle cx="10" cy="27" r="4"/><circle cx="36" cy="27" r="4"/></svg>
    Acquire more development capacity and get results fast
  </div>
  <div class="consult-card">
    <svg width="40" height="36" viewBox="0 0 40 36" fill="none" stroke="#333" stroke-width="2"><rect x="4" y="6" width="32" height="26"/><path d="M4 14h32M12 2v8M28 2v8"/></svg>
    Avoid the overhead incurred by frequent scaling of your development team
  </div>
  <div class="consult-card">
    <svg width="56" height="30" viewBox="0 0 56 30" fill="none" stroke="#333" stroke-width="2"><path d="M6 24l14-14 14 10 16-14"/><circle cx="6" cy="24" r="4" fill="#fff"/><circle cx="20" cy="10" r="4" fill="#fff"/><circle cx="34" cy="20" r="4" fill="#fff"/><circle cx="50" cy="6" r="4" fill="#fff"/></svg>
    Reach a wide spectrum of expertise
  </div>
</section>

<section class="portfolio" role="img" aria-label="Photo of a red truck on a motorway at sunset">
  <h2 class="portfolio-title">PORTFOLIO</h2>
  <div class="portfolio-panel">
    <h3>VESTIBULUM CONDIMENTUM</h3>
    <p>We design, build and support systems for clients across logistics, retail and finance, from first prototype through to live operation.</p>
    <a class="btn-outline">Read more</a>
  </div>
</section>

<h2 class="section-title about-title">ABOUT US</h2>
<p class="about-text">Aliquam erat volutpat. Quisque aliquet eu nisi vel vestibulum pulvinar. Pellentesque convallis molestie enim sit amet efficitur. Etiam id mi porttitor lectus. Vivamus lacus justo, ultrices nec erat in, euismod iaculis massa. Vivamus eleifend vitae nulla vel malesuada. Ut ac malesuada lacus, et consectetur ante. Fusce vitae lectus sit amet mi pulvinar maximus.</p>

<footer>
  <div class="footer-bar">
    <span class="item"><svg width="12" height="16" viewBox="0 0 12 16"><path d="M6 1a5 5 0 0 1 5 5c0 4-5 9-5 9S1 10 1 6a5 5 0 0 1 5-5z" fill="#fff"/></svg>18 Harbour Lane, Millbrook, Eastfield - 40210</span>
    <span class="item"><svg width="14" height="14" viewBox="0 0 14 14"><path d="M3 1l3 3-2 2c1 2 2 3 4 4l2-2 3 3-2 2C6 13 1 8 1 3z" fill="#fff"/></svg>+44 20 7946 0321</span>
    <span class="item"><svg width="16" height="12" viewBox="0 0 16 12"><rect x="1" y="1" width="14" height="10" fill="none" stroke="#fff" stroke-width="1.5"/><path d="M1 1l7 6 7-6" fill="none" stroke="#fff" stroke-width="1.5"/></svg>info@korvelsolutions.com</span>
    <span class="social"><span></span><span></span><span></span><span></span><span></span></span>
  </div>
  <div class="footer-bottom">
    <nav class="footer-nav"><a href="#">Home</a>|<a href="#">Korvel Futures</a>|<a href="#">IT consultancy</a>|<a href="#">About Us</a>|<a href="#">Contact Us</a></nav>
    <p>Copyright © 2016 Korvel Solutions - All rights reserved</p>
  </div>
</footer>

</body>
</html>
```